Tr construction holdings pty ltd

2 sided card black and red with white
Very professional and elegant

Target Market(s)

Construction and Development

Industry/Entity Type

Construction and development

Contact Information for Business Card

One side black, one side red/or white business logo in top corner, email: morgan@trbuildworks.example

Requirements
Should not have
• Blue

```html
<!DOCTYPE html>
<html lang="en">
<head>
<meta charset="utf-8">
<title>TR Construction – Business Card</title>
<link rel="stylesheet" href="https://fonts.googleapis.com/css2?family=Montserrat:wght@400;500;600;700&display=swap">
<style>
  :root {
    --backdrop: #77767b;
    --card-black: #131313;
    --brand-red: #e63f24;
    --paper-white: #ffffff;
    --muted-white: #e9e9e9;
  }
  html, body {
    margin: 0;
    width: 1200px;
    height: 900px;
    overflow: hidden;
    background: var(--backdrop);
    font-family: "Montserrat", Arial, sans-serif;
  }
  .canvas {
    position: relative;
    width: 1200px;
    height: 900px;
  }
  .card {
    position: absolute;
    left: 320px;
    width: 560px;
    height: 320px;
    border-radius: 16px;
    overflow: hidden;
    box-shadow: 0 6px 18px rgba(0,0,0,0.25);
  }
  .card--front { top: 80px; background: var(--card-black); }
  .card--back  { top: 480px; background: var(--brand-red); }

  .card__bands { position: absolute; inset: 0; }

  .brand {
    position: absolute;
    display: flex;
    align-items: center;
    gap: 10px;
    font-weight: 700;
    letter-spacing: 2px;
    text-transform: uppercase;
    white-space: nowrap;
  }
  .brand__mark { width: 12px; height: 12px; }
  .card--front .brand {
    left: 190px; top: 92px;
    font-size: 30px;
    color: var(--paper-white);
  }
  .card--front .brand__mark { background: var(--brand-red); }
  .card--back .brand {
    left: 0; right: 0; top: 138px;
    justify-content: center;
    font-size: 38px;
    color: var(--paper-white);
  }
  .card--back .brand__mark { background: var(--card-black); width: 14px; height: 14px; }

  .deco-block {
    position: absolute;
    left: 28px; top: 48px;
    width: 110px; height: 130px;
    background: var(--brand-red);
  }

  .holder {
    position: absolute;
    left: 40px; top: 218px;
  }
  .holder__name {
    display: inline-block;
    background: var(--brand-red);
    color: var(--paper-white);
    font-weight: 600;
    font-size: 15px;
    letter-spacing: 1px;
    padding: 4px 14px;
  }
  .contact {
    display: flex;
    align-items: center;
    gap: 8px;
    color: var(--muted-white);
    font-size: 13px;
    letter-spacing: 0.5px;
  }
  .holder .contact { margin-top: 8px; }
  .contact__icon {
    width: 18px; height: 18px;
    display: flex; align-items: center; justify-content: center;
  }
  .contact__icon--phone { background: var(--brand-red); }
  .contact__icon--mail { border: 1.5px solid var(--paper-white); box-sizing: border-box; }

  .email-block {
    position: absolute;
    left: 330px; top: 212px;
    width: 215px;
  }
  .email-block__rule {
    height: 1px;
    background: var(--muted-white);
    margin-bottom: 12px;
  }
  .email-block .contact { font-size: 12px; }
</style>
</head>
<body>
<main class="canvas">

  <section class="card card--front" aria-label="Card front">
    <svg class="card__bands" width="560" height="320" viewBox="0 0 560 320" aria-hidden="true">
      <polygon points="0,150 28,150 28,178 0,178" fill="#e63f24"/>
      <line x1="140" y1="258" x2="330" y2="258" stroke="#e63f24" stroke-width="1.5"/>
      <polygon points="345,282 560,282 560,320 320,320" fill="#e63f24"/>
      <polygon points="0,304 312,304 304,320 0,320" fill="#ffffff"/>
      <polygon points="0,184 60,184 60,198 0,198" fill="#ffffff"/>
    </svg>

    <div class="deco-block" role="img" aria-label="Large brand block decoration"></div>

    <div class="brand">
      <span>TR Construction</span><span class="brand__mark"></span>
    </div>

    <div class="holder">
      <div class="holder__name">MORGAN</div>
      <div class="contact">
        <span class="contact__icon contact__icon--phone">
          <svg width="11" height="11" viewBox="0 0 24 24" aria-hidden="true"><path fill="#fff" d="M6.6 10.8a15 15 0 0 0 6.6 6.6l2.2-2.2a1 1 0 0 1 1-.25 11.4 11.4 0 0 0 3.6.57 1 1 0 0 1 1 1V20a1 1 0 0 1-1 1A17 17 0 0 1 3 4a1 1 0 0 1 1-1h3.5a1 1 0 0 1 1 1c0 1.25.2 2.45.57 3.57a1 1 0 0 1-.25 1z"/></svg>
        </span>
        <span>555-014-2290</span>
      </div>
    </div>

    <div class="email-block">
      <div class="email-block__rule"></div>
      <div class="contact">
        <span class="contact__icon contact__icon--mail">
          <svg width="11" height="9" viewBox="0 0 22 16" aria-hidden="true"><path d="M1 1h20v14H1z M1 1l10 8 10-8" fill="none" stroke="#fff" stroke-width="2"/></svg>
        </span>
        <span>morgan@trbuildworks.example</span>
      </div>
    </div>
  </section>

  <section class="card card--back" aria-label="Card back">
    <div class="brand">
      <span>TR Construction</span><span class="brand__mark"></span>
    </div>
  </section>

</main>
</body>
</html>
```